Customizable Gift Note Card Design

I need a gift note card designed for my Healthy Snacks Care Package company. I need to be able to customize each card with the customer's gift message to the recipient and print to a standard printer.

The card should be single-sided 5 x 7, include our logo, keep colors and graphics simple since they will be printed for each individual order on a standard printer. I would like the following quote to be included in a small and subtle way: "Food is symbolic of love when words are inadequate." —Bertram K. Osslund. Our website thebrightpantrybites.example should also be included.

I have included pictures of our product packaging for reference.

Target Market(s)

Gift recipients: Students, people recovering from illness, housewarming, thank you gifts...etc.

Industry/Entity Type

It Company

Colors

Designer to choose colors to be used in the design.

Requirements
Must have
• We are looking for a simple, cute and elegant gift card that reflects our branding. Must be customizable and printable on a standard printer.
• Must be single-sided 5x7.

```html
<!DOCTYPE html>
<html lang="en">
<head>
<meta charset="utf-8">
<title>The Bright Pantry – Gift Note Card</title>
<link rel="stylesheet" href="https://fonts.googleapis.com/css2?family=Open+Sans:wght@400;700&display=swap">
<style>
  :root {
    --paper: #ffffff;
    --brand-red: #8c0a10;
    --band-red: #9a0d14;
    --band-deep: #6e0509;
    --bright-red: #b0141c;
    --ink: #111111;
    --kraft: #c9a57a;
    --kraft-light: #d6b88f;
    --text-red: #8a0b10;
    --text-dark: #2a2a2a;
  }
  html, body {
    margin: 0;
    padding: 0;
    overflow: hidden;
    background: var(--paper);
  }
  .card {
    position: relative;
    width: 1200px;
    height: 857px;
    background: var(--paper);
    overflow: hidden;
    font-family: "Open Sans", Arial, sans-serif;
  }
  .card__art {
    position: absolute;
    inset: 0;
    width: 1200px;
    height: 857px;
  }
  .quote {
    position: absolute;
    left: 130px;
    top: 292px;
    width: 560px;
    text-align: center;
    margin: 0;
  }
  .quote__text {
    margin: 0;
    color: var(--text-red);
    font-weight: 700;
    font-size: 30px;
    line-height: 38px;
  }
  .quote__author {
    display: block;
    margin-top: 2px;
    color: var(--text-red);
    font-weight: 400;
    font-size: 18px;
    line-height: 24px;
  }
  .brand {
    position: absolute;
    left: 48px;
    top: 726px;
    display: flex;
    align-items: center;
    gap: 12px;
  }
  .brand__dot {
    width: 34px;
    height: 34px;
    border-radius: 50%;
    background: var(--ink);
  }
  .brand__name {
    color: var(--text-dark);
    font-weight: 700;
    font-size: 24px;
    letter-spacing: 0.3px;
  }
  .site-ribbon {
    position: absolute;
    left: 0;
    top: 790px;
    width: 400px;
    height: 44px;
  }
  .site-ribbon__url {
    position: absolute;
    left: 46px;
    top: 799px;
    margin: 0;
    color: #ffffff;
    font-size: 17px;
    line-height: 26px;
    letter-spacing: 0.3px;
  }
</style>
</head>
<body>
<main class="card">
  <svg class="card__art" viewBox="0 0 1200 857" aria-hidden="false">
    <defs>
      <linearGradient id="band-glow" x1="0" y1="0" x2="0" y2="1">
        <stop offset="0" stop-color="var(--band-red)"/>
        <stop offset="1" stop-color="var(--bright-red)"/>
      </linearGradient>
      <linearGradient id="kraft-tone" x1="0" y1="0" x2="1" y2="1">
        <stop offset="0" stop-color="var(--kraft-light)"/>
        <stop offset="1" stop-color="var(--kraft)"/>
      </linearGradient>
    </defs>
    <polygon class="corner-wedge" points="895,0 1105,0 1011,170" fill="var(--ink)"/>
    <polygon class="band band--outer" points="1105,0 1200,0 1200,857 630,857" fill="var(--brand-red)"/>
    <polygon class="band band--shadow" points="1150,0 1170,0 728,857 708,857" fill="var(--band-deep)" opacity="0.55"/>
    <polygon class="band band--inner" points="1170,0 1200,0 1200,857 728,857" fill="var(--band-red)"/>
    <polygon class="band band--lower" points="925,668 1060,857 728,857 820,680" fill="url(#band-glow)"/>
    <polygon class="band band--shadow" points="1200,120 1200,150 925,668 905,660" fill="var(--band-deep)" opacity="0.6"/>
    <polygon class="kraft-panel" role="img" aria-label="Kraft paper texture with the brand mascot illustration"
             points="1200,150 1200,857 1060,857 925,668" fill="url(#kraft-tone)"/>
    <polygon class="site-ribbon" points="0,790 400,790 372,812 400,834 0,834" fill="var(--brand-red)"/>
  </svg>

  <blockquote class="quote">
    <p class="quote__text">"Food is symbolic of love<br>when words are inadequate."</p>
    <cite class="quote__author">—Bertram K. Osslund</cite>
  </blockquote>

  <div class="brand">
    <span class="brand__dot"></span>
    <span class="brand__name">The Bright Pantry</span>
  </div>

  <p class="site-ribbon__url">www.thebrightpantrybites.example/</p>
</main>
</body>
</html>
```